Summit Homes Collective Business Card

We are looking for a simple clean real estate business card design that includes the following information:

Front of card (2):

Front 1:

Photo of Mark (with the background cut out) on the front

Summit Logo at the top

Small Harbor Keystone logo at the bottom

Mark Volkin
555.218.4071
MarkVolkin@harborkeystone-mail.ca
#4, 2719 - 31St. Red Deer, Ab T0X 1Z2

Front 1:

Photo of Glen (with the background cut out) on the front

Summit Logo at the top

Mark Volkin
555.274.9186
MarkVolkin@harborkeystone-mail.ca

Back of card (for both cards):
**very simple and plain with the SUMMIT LOGO faded in the background**

Your Home Sold GUARANTEED Or We'll Buy It Or Sell It For Free...Your Choice

Buy Any Property With Us And If You're Not 100% Satisfied We'll Sell It For Free!

```html
<!DOCTYPE html>
<html lang="en">
<head>
<meta charset="utf-8">
<title>Summit Homes Collective Business Cards</title>
<link href="https://fonts.googleapis.com/css2?family=Arimo:ital,wght@0,400;0,700;1,400;1,700&display=swap" rel="stylesheet">
<style>
  :root {
    --brand-red: #a3161b;
    --card-white: #ffffff;
    --suit-black: #141416;
    --text-grey: #4a4a4a;
    --info-text: #3c3c3c;
    --name-red: #c8262b;
    --faded-brand: #c98a76;
  }
  * { box-sizing: border-box; margin: 0; padding: 0; }
  html, body { width: 1166px; height: 1200px; overflow: hidden; }
  body {
    position: relative;
    font-family: "Arimo", Arial, sans-serif;
    background: radial-gradient(ellipse 70% 60% at 33% 60%, #e8e8e8 0%, #a9a9a9 40%, #505050 75%, #262626 100%);
  }
  .card {
    position: absolute;
    background: var(--card-white);
    overflow: hidden;
  }
  .card--front-mark { left: 105px; top: 48px; width: 309px; height: 543px; }
  .card--front-glen { left: 105px; top: 627px; width: 309px; height: 542px; }
  .card--back { left: 508px; top: 84px; width: 586px; height: 1038px; }

  .brand {
    position: absolute;
    display: flex;
    align-items: center;
    gap: 8px;
  }
  .brand__dot {
    width: 54px; height: 54px;
    border-radius: 50%;
    background: var(--brand-red);
  }
  .brand__name {
    font-weight: 700;
    font-size: 34px;
    color: var(--brand-red);
    letter-spacing: 0.5px;
  }
  .card--front-mark .brand,
  .card--front-glen .brand { left: 45px; top: 12px; }

  .agent-photo {
    position: absolute;
    border-radius: 46% 46% 0 0 / 22% 22% 0 0;
    background: linear-gradient(to bottom, #efe3da 0%, #c8977a 14%, #b8876b 30%, #e9e9e9 42%, #1f1f22 52%, var(--suit-black) 100%);
  }
  .card--front-mark .agent-photo { left: 20px; top: 72px; width: 270px; height: 471px; }
  .card--front-glen .agent-photo { left: 20px; top: 62px; width: 270px; height: 480px; }

  .info-box {
    position: absolute;
    left: 0; top: 366px;
    width: 250px; height: 78px;
    background: rgba(212, 212, 212, 0.72);
    padding: 10px 0 0 16px;
    color: var(--info-text);
    font-size: 11px;
    line-height: 14.5px;
    white-space: nowrap;
  }

  .partner {
    position: absolute;
    display: flex;
    align-items: center;
    gap: 4px;
    font-size: 8px;
    font-weight: 700;
    color: #ffffff;
    letter-spacing: 0.3px;
    white-space: nowrap;
  }
  .partner__mark { width: 10px; height: 10px; background: var(--brand-red); }
  .card--front-mark .partner { right: 24px; top: 507px; }
  .card--front-glen .partner { left: 0; right: 0; top: 498px; justify-content: center; }

  .contact-center {
    position: absolute;
    left: 0; right: 0; top: 406px;
    text-align: center;
    color: #ffffff;
    font-size: 11.5px;
    line-height: 13.5px;
    white-space: nowrap;
  }
  .contact-center__name { color: var(--name-red); }

  .card--back .brand {
    left: 0; right: 0; top: 506px;
    justify-content: center;
    opacity: 0.55;
  }
  .card--back .brand__dot { width: 56px; height: 56px; background: var(--faded-brand); }
  .card--back .brand__name { color: var(--faded-brand); font-size: 30px; }

  .pledge {
    position: absolute;
    left: 0; right: 0;
    text-align: center;
    font-style: italic;
    font-size: 16.5px;
    line-height: 21px;
    letter-spacing: 1.2px;
    color: var(--text-grey);
  }
  .pledge strong { font-weight: 700; color: #2b2b2b; }
  .pledge--sale { top: 585px; }
  .pledge--purchase { top: 647px; }
</style>
</head>
<body>

  <section class="card card--front-mark">
    <div class="brand">
      <span class="brand__dot"></span>
      <span class="brand__name">SUMMIT</span>
    </div>
    <div class="agent-photo" role="img" aria-label="Cut-out portrait photo of Mark in a dark suit and white shirt"></div>
    <div class="info-box">
      <p>Mark Volkin</p>
      <p>555.218.4071</p>
      <p>MarkVolkin@harborkeystone-mail.ca</p>
      <p>#4, 2719 - 31St. Red Deer, Ab T0X 1Z2</p>
    </div>
    <div class="partner">
      <span class="partner__mark"></span>
      <span>HARBOR KEYSTONE</span>
    </div>
  </section>

  <section class="card card--front-glen">
    <div class="brand">
      <span class="brand__dot"></span>
      <span class="brand__name">SUMMIT</span>
    </div>
    <div class="agent-photo" role="img" aria-label="Cut-out portrait photo of Glen in a dark suit and white shirt"></div>
    <div class="contact-center">
      <p class="contact-center__name">Glen Albrook</p>
      <p>555.274.9186</p>
      <p>GlenAlbrook@harborkeystone-mail.ca</p>
      <p>#4, 2719 - 31St. Red Deer,</p>
      <p>Ab T0X 1Z2</p>
    </div>
    <div class="partner">
      <span class="partner__mark"></span>
      <span>HARBOR KEYSTONE</span>
    </div>
  </section>

  <section class="card card--back">
    <div class="brand">
      <span class="brand__dot"></span>
      <span class="brand__name">SUMMIT</span>
    </div>
    <p class="pledge pledge--sale">Your Home <strong>Sold GUARANTEED</strong> Or We'll Buy<br>It Or <strong>Sell It For Free</strong>...Your Choice</p>
    <p class="pledge pledge--purchase"><strong>Buy</strong> Any Property With Us And If You're Not<br>100% Satisfied We'll <strong>Sell It For Free</strong>!</p>
  </section>

</body>
</html>
```